Graphical design for food product in 1 Liter carton

We need this design not for a real product but as a showcase for a new service.

This special situation makes it really simple for you to participate because you only have to care about how the visual impression of your design is.

Furthermore it gives you the opportunity to get an extra winning chance if you choose to also participate in the open competition at our website - where you can enter the same design as you enter here at ArtQuarry.

Here is the requirements:

1. You must apply your design to our attatched template

2. Make a design for a food product of your own choice, which is to be sold from retail stores in a rectangular 1 L carton – based on our template.

3. You are only allowed to use brand names and/or logos that you have the rights to use for this competition, so please make completely fictive brand names and logos.

4. Your design is evaluated on the visual impression only, which means that your text on the design can be in any language and doesn’t have to relate to the design.

5. The criteria for the evaluation of your design is your creativity, the graphical quality and how well the product will display it self in the stores.

If you also want to participate in the open competition on our website - where you can win an Zelbo Slate, and will get your design skills exposed to brand owners and packaging manufacturers all over the world, then please visit plovimark.example/packaging-design-competition/

Attatched is:

A. Empty design template you must apply your design to. Remove the layer with our template when you return your send in your design.

B. Example of design applied to the template.

C. Example of the applied example design after it has been converted to 3D with our online 3D engine at PloviMark.example.

The winning design will be converted to 3D and will be used as a showcase on our website - all designers can enter their design to our open competition at PloviMark.example.

```html
<!DOCTYPE html>
<html lang="en">
<head>
<meta charset="utf-8">
<title>Lean Ladle Kitchen – Organic Soup carton front</title>
<link href="https://fonts.googleapis.com/css2?family=PT+Sans:wght@400;700&display=swap" rel="stylesheet">
<style>
  :root {
    --page: #ffffff;
    --cream: #f8f1d2;
    --maroon: #8e1a1f;
    --maroon-light: #b8343a;
    --ink: #3a2a20;
    --tag-red: #d42a2a;
    --tag-orange: #ee8a26;
    --tag-green: #9cc03c;
    --ring: #f2a51c;
    --white: #ffffff;
  }
  html, body {
    margin: 0;
    width: 1200px;
    height: 966px;
    overflow: hidden;
    background: var(--page);
    font-family: "PT Sans", sans-serif;
  }
  .carton-front {
    position: absolute;
    left: 454px;
    top: 72px;
    width: 292px;
    height: 822px;
    background: var(--cream);
    overflow: hidden;
  }
  .carton-art {
    position: absolute;
    inset: 0;
  }
  .brand-name {
    position: absolute;
    top: 28px;
    left: 0;
    width: 292px;
    text-align: center;
    color: var(--white);
    font-weight: 700;
    font-size: 22px;
    letter-spacing: 0.2px;
  }
  .product-title {
    position: absolute;
    top: 130px;
    left: 14px;
    width: 180px;
    margin: 0;
    text-align: center;
    color: var(--maroon);
    font-weight: 700;
    font-size: 42px;
    line-height: 44px;
  }
  .product-tagline {
    position: absolute;
    top: 233px;
    left: 20px;
    margin: 0;
    color: var(--ink);
    font-size: 14px;
  }
  .claim-tags {
    position: absolute;
    top: 266px;
    left: 10px;
    display: flex;
    gap: 11px;
    margin: 0;
    padding: 0;
    list-style: none;
  }
  .claim-tag {
    width: 58px;
    height: 66px;
    display: flex;
    align-items: center;
    justify-content: center;
    text-align: center;
    color: var(--white);
    font-weight: 700;
    font-size: 13px;
    line-height: 15px;
    box-shadow: inset 0 6px 0 rgba(255,255,255,0.25);
  }
  .claim-tag--carbs { background: var(--tag-red); }
  .claim-tag--calories { background: var(--tag-orange); font-size: 11px; }
  .claim-tag--fat { background: var(--tag-green); }
  .natural-seal {
    position: absolute;
    left: 22px;
    top: 628px;
    width: 84px;
    height: 84px;
    border-radius: 50%;
    background: radial-gradient(circle at 40% 35%, #ffc64a, #e97a12 70%);
    box-shadow: 0 0 0 6px #fbe9c6, 0 0 0 7px #e3b37a;
    display: flex;
    flex-direction: column;
    align-items: center;
    justify-content: center;
    color: var(--white);
    font-weight: 700;
  }
  .natural-seal__percent { font-size: 26px; line-height: 26px; }
  .natural-seal__word { font-size: 13px; line-height: 15px; }
  .net-content {
    position: absolute;
    left: 0;
    bottom: 0;
    width: 292px;
    height: 64px;
    background: var(--maroon);
    color: var(--white);
    font-weight: 700;
    font-size: 24px;
    line-height: 64px;
    text-align: center;
  }
</style>
</head>
<body>
  <main class="carton-front">
    <svg class="carton-art" width="292" height="822" viewBox="0 0 292 822" aria-hidden="false">
      <defs>
        <linearGradient id="veg-tones" x1="0" y1="0" x2="0" y2="1">
          <stop offset="0" stop-color="#6f9b3a"/>
          <stop offset="0.3" stop-color="#c8462e"/>
          <stop offset="0.5" stop-color="#e9a23a"/>
          <stop offset="0.7" stop-color="#d9d3c2"/>
          <stop offset="1" stop-color="#4f7d2c"/>
        </linearGradient>
        <linearGradient id="vine-tones" x1="0" y1="0" x2="1" y2="1">
          <stop offset="0" stop-color="#dfe2b0" stop-opacity="0.55"/>
          <stop offset="1" stop-color="#dfe2b0" stop-opacity="0.15"/>
        </linearGradient>
      </defs>
      <rect class="vine-pattern" x="0" y="60" width="292" height="698" fill="url(#vine-tones)" role="img" aria-label="Faint leafy vine pattern across the cream background"/>
      <path class="brand-arch" d="M0,0 H292 V62 Q146,104 0,62 Z" fill="var(--maroon)"/>
      <path class="brand-arch-line" d="M18,72 Q146,110 274,72" fill="none" stroke="var(--maroon-light)" stroke-width="2"/>
      <path class="vegetable-swoosh" d="M158,92 C228,190 196,420 212,540 C222,620 250,680 292,720 L292,92 Z" fill="url(#veg-tones)" role="img" aria-label="Photo of fresh vegetables: tomatoes, peppers, mushrooms and herbs"/>
      <g class="ring-decor" fill="none" stroke="var(--ring)" stroke-width="6">
        <circle cx="72" cy="420" r="52"/>
        <circle cx="112" cy="525" r="42"/>
        <circle cx="30" cy="510" r="26"/>
        <circle cx="75" cy="600" r="22"/>
      </g>
    </svg>

    <div class="brand-name">Lean Ladle Kitchen</div>
    <h1 class="product-title">Organic<br>Soup</h1>
    <p class="product-tagline">Ready to eat in 2 min</p>
    <ul class="claim-tags">
      <li class="claim-tag claim-tag--carbs">NO<br>CARBS</li>
      <li class="claim-tag claim-tag--calories">LOW<br>CALORIES</li>
      <li class="claim-tag claim-tag--fat">FAT<br>FREE</li>
    </ul>
    <div class="natural-seal">
      <span class="natural-seal__percent">100%</span>
      <span class="natural-seal__word">NATURAL</span>
    </div>
    <div class="net-content">NET 32 FL OZ 250g</div>
  </main>
</body>
</html>
```